Pipelining Product Supply Company Needs New Stationery

We need new stationery (letter head, with compliments slips & business card) for our industry leading pipe lining supply company. basically we sell product to other plumbers to carry out pipe relining.

Im looking for something, fresh, professional, sleek and modern at the same time.

Ive attached a copy of the logo and also some guidelines to follow for colours and fonts etc.

Target Market(s)

Plumbers

Industry/Entity Type

Plumbing

Font styles to use
Sans Serif

Requirements
Must have
• The logo, space for ABN, Address, Phone Number, website and email.
Nice to have
• Stand out from the crowd. To look sleep and professional.
Should not have
• Any other colours apart from what is on the guidelines.

```html
<!DOCTYPE html>
<html lang="en">
<head>
<meta charset="utf-8">
<title>Reline Supply Co – Business Card</title>
<link href="https://fonts.googleapis.com/css2?family=Roboto:wght@400;500;700&display=swap" rel="stylesheet">
<style>
  :root {
    --backdrop: #2a2a2a;
    --card-white: #f3f3f3;
    --band-grey: #9a9b9d;
    --green-dark: #0f4f0f;
    --green-mid: #3f8f22;
    --green-light: #8cc63f;
    --text-white: #ffffff;
  }
  * { margin: 0; padding: 0; box-sizing: border-box; }
  html, body { width: 1200px; height: 960px; overflow: hidden; }
  body {
    background: var(--backdrop);
    font-family: "Roboto", Arial, sans-serif;
    position: relative;
  }
  .card {
    position: absolute;
    width: 600px;
    height: 342px;
    border-radius: 20px;
    overflow: hidden;
  }
  .card-front { left: 302px; top: 129px; background: var(--card-white); }
  .card-back {
    left: 300px; top: 488px; width: 598px;
    background: radial-gradient(ellipse 58% 70% at 50% 50%, var(--green-light) 0%, var(--green-mid) 50%, var(--green-dark) 100%);
  }
  .front-wave { position: absolute; inset: 0; width: 100%; height: 100%; }
  .brand-name {
    position: absolute;
    left: 52px; top: 70px;
    font-weight: 700;
    font-size: 30px;
    line-height: 1.15;
    letter-spacing: 1px;
    color: var(--green-mid);
    text-transform: uppercase;
  }
  .contact-block {
    position: absolute;
    right: 42px; top: 136px;
    text-align: right;
    color: var(--text-white);
    font-size: 14px;
    line-height: 17px;
  }
  .contact-name { font-size: 20px; font-weight: 700; line-height: 24px; }
  .contact-title { font-size: 14px; font-weight: 700; margin-bottom: 12px; }
  .contact-address { margin-bottom: 3px; }
  .contact-abn { margin-bottom: 10px; }
  .contact-line { display: flex; justify-content: flex-end; align-items: center; gap: 6px; height: 18px; }
  .contact-line svg { width: 13px; height: 13px; fill: var(--text-white); }
  .back-brand {
    position: absolute;
    left: 0; right: 0; top: 118px;
    text-align: center;
    font-weight: 700;
    font-size: 50px;
    letter-spacing: 2px;
    color: #c9e89a;
    text-transform: uppercase;
  }
  .back-web {
    position: absolute;
    left: 0; right: 0; top: 216px;
    text-align: center;
    font-size: 14px;
    letter-spacing: 1.5px;
    color: var(--text-white);
  }
</style>
</head>
<body>
  <section class="card card-front">
    <svg class="front-wave" viewBox="0 0 600 342" preserveAspectRatio="none" aria-hidden="true">
      <path d="M0,245 C60,300 140,322 200,312 C270,300 320,200 380,140 C440,85 520,74 600,78 L600,342 L0,342 Z" fill="var(--band-grey)"/>
      <path d="M0,245 C60,300 140,322 200,312 C270,300 320,200 380,140 C440,85 520,74 600,78" fill="none" stroke="#ffffff" stroke-width="6"/>
      <path d="M0,240 C60,292 140,314 200,304 C270,292 320,193 380,134 C440,80 520,70 600,74" fill="none" stroke="var(--green-mid)" stroke-width="5"/>
    </svg>
    <div class="brand-name">Reline<br>Supply Co</div>
    <div class="contact-block">
      <div class="contact-name">DANIEL REYES</div>
      <div class="contact-title">CEO/FOUNDER</div>
      <div class="contact-address">42 Harbour Street<br>Geelong, Victoria 3220</div>
      <div class="contact-abn">ABN: 9081726354</div>
      <div class="contact-line">031 555 0184
        <svg viewBox="0 0 24 24" aria-hidden="true"><path d="M6.6 10.8a15 15 0 0 0 6.6 6.6l2.2-2.2a1 1 0 0 1 1-.25 11.4 11.4 0 0 0 3.6.57 1 1 0 0 1 1 1V20a1 1 0 0 1-1 1A17 17 0 0 1 3 4a1 1 0 0 1 1-1h3.5a1 1 0 0 1 1 1c0 1.25.2 2.45.57 3.57a1 1 0 0 1-.25 1z"/></svg>
      </div>
      <div class="contact-line">hello@relinesupply.com
        <svg viewBox="0 0 24 24" aria-hidden="true"><path d="M2 5h20v14H2z M3 6l9 7 9-7" fill="#fff" stroke="var(--band-grey)" stroke-width="1.5"/></svg>
      </div>
      <div class="contact-line">www.relinesupply.com
        <svg viewBox="0 0 24 24" aria-hidden="true"><circle cx="12" cy="12" r="10"/><path d="M2 12h20M12 2c3 3 3 17 0 20M12 2c-3 3-3 17 0 20" fill="none" stroke="var(--band-grey)" stroke-width="1.5"/></svg>
      </div>
    </div>
  </section>

  <section class="card card-back">
    <div class="back-brand">Reline Supply Co</div>
    <div class="back-web">www.relinesupplyco.com.au</div>
  </section>
</body>
</html>
```